Veltrium stationery design

Design stationery for us that fits with the colours of the logo. We are looking for letterheads, business cards etc. Something we can use for a prospectus and marketing presentations in power point. Must be completed in such a manner that it represents a corporate image for large enterprise clients and other large organisations. The company is a project assurance and monitoring company that works in all industries.

```html
<!DOCTYPE html>
<html lang="en">
<head>
<meta charset="utf-8">
<title>Veltrium Stationery</title>
<link href="https://fonts.googleapis.com/css2?family=Inter:wght@400;500;600;700;800&family=Montserrat:wght@800&display=swap" rel="stylesheet">
<style>
:root{
  --navy:#0b2e6f;
  --navy-deep:#16306a;
  --blue:#1d4f9f;
  --blue-light:#3f73c4;
  --red:#f5260a;
  --orange:#ff6a00;
  --ink:#232323;
  --muted:#6b6b6b;
  --stage:#dedede;
  --paper:#ffffff;
}
*{margin:0;padding:0;box-sizing:border-box}
html,body{width:873px;height:1200px;overflow:hidden;background:var(--paper)}
body{position:relative;font-family:"Inter",Arial,sans-serif;color:var(--ink)}
.stage{position:absolute;inset:0}
.abs{position:absolute}
.section-label{position:absolute;font-family:"Montserrat",Arial,sans-serif;font-weight:800;font-size:12px;letter-spacing:3.6px;color:#3b3b3b}
.sheet{position:absolute;background:var(--paper);box-shadow:0 1px 4px rgba(0,0,0,.18);overflow:hidden}
.sheet svg.art{position:absolute;inset:0;width:100%;height:100%}
.brand{position:absolute;display:flex;align-items:center;gap:4px;font-weight:700;color:var(--navy);white-space:nowrap}
.brand .dot{border-radius:50%;background:var(--orange);flex:none}
.contact{position:absolute;font-size:6px;line-height:1.25;color:var(--ink)}
.contact .row{position:absolute;left:0;white-space:nowrap}
.contact svg{position:absolute;width:5px;height:5px}
.body-copy{position:absolute;color:#444;text-align:justify}
/* letterhead */
.lh-to{position:absolute;left:19px;top:108px;line-height:1.15}
.lh-to .small{font-size:4.2px;color:#555}
.lh-to .strong{font-size:7px;font-weight:600;color:var(--ink)}
.lh-body{left:18px;top:182px;width:238px;font-size:4.1px;line-height:5.4px}
.lh-body p{margin-bottom:5px}
.lh-sign{position:absolute;left:19px;top:280px;width:52px;height:22px;background:linear-gradient(90deg,#eee,#f7f7f7);border-radius:3px}
.lh-sign-line{position:absolute;left:19px;top:308px;width:49px;height:1px;background:#333}
/* headings */
.headline{position:absolute;font-weight:800;color:var(--navy);letter-spacing:-.2px}
.subline{position:absolute;font-weight:500;color:var(--orange);line-height:1.15}
.rule{position:absolute;height:1px;background:#999}
.feature{position:absolute;color:#fff}
.feature h4{font-weight:400;font-size:11px;line-height:1}
.feature p{font-size:4.2px;line-height:5px;margin-top:2px;text-align:justify}
.mini-icon{position:absolute;color:#fff;font-size:3.6px;text-align:center;width:34px}
.list-item{position:absolute;left:22px;display:flex;gap:6px;align-items:center}
.list-item .ring{width:22px;height:22px;border-radius:50%;display:flex;align-items:center;justify-content:center;flex:none}
.list-item h5{font-size:5.3px;font-weight:700;color:var(--navy)}
.list-item p{font-size:2.8px;line-height:3.4px;color:#777;width:58px}
</style>
</head>
<body>
<div class="stage">
  <svg class="abs" width="873" height="1200" style="left:0;top:0">
    <polygon points="873,5 873,1200 0,1200 0,1163" fill="var(--stage)"/>
  </svg>

  <!-- Letterhead -->
  <div class="section-label" style="left:117px;top:54px">LETTERHEAD</div>
  <div class="sheet letterhead" style="left:109px;top:88px;width:282px;height:398px">
    <svg class="art" viewBox="0 0 282 398" preserveAspectRatio="none">
      <circle cx="148" cy="277" r="58" fill="#f1f1f1"/>
      <path d="M72 398 Q190 372 282 318 L282 338 Q200 382 120 398Z" fill="var(--red)"/>
      <path d="M110 398 Q210 376 282 330 L282 340 Q215 380 140 398Z" fill="var(--orange)"/>
      <path d="M140 398 Q220 378 282 340 L282 398Z" fill="var(--blue)"/>
    </svg>
    <div class="brand" style="left:20px;top:44px;font-size:12px"><span class="dot" style="width:10px;height:10px"></span>Veltrium</div>
    <div class="contact" style="left:186px;top:29px;width:90px;height:45px">
      <svg style="left:-8px;top:1px" viewBox="0 0 10 10"><path d="M2 1l2 0 1 2-1 1q1 2 3 3l1-1 2 1 0 2q-7 0-8-8z" fill="var(--orange)"/></svg>
      <div class="row" style="top:0">(123) 456-789</div>
      <svg style="left:-8px;top:15px" viewBox="0 0 10 10"><rect x="1" y="2" width="8" height="6" fill="var(--orange)"/><path d="M1 2l4 3 4-3" stroke="#fff" fill="none" stroke-width=".8"/></svg>
      <div class="row" style="top:14px">email@veltrium.com</div>
      <svg style="left:-8px;top:31px" viewBox="0 0 10 10"><path d="M5 9Q1 5 1 3.5a4 4 0 0 1 8 0Q9 5 5 9z" fill="var(--orange)"/><circle cx="5" cy="3.5" r="1.3" fill="#fff"/></svg>
      <div class="row" style="top:26px">Your Address Here<br>United States, 00000</div>
    </div>
    <div class="lh-to">
      <div class="small">To</div>
      <div class="strong">Name Surname</div>
      <div class="small">Position Here</div>
      <div class="strong" style="margin-top:7px">Company Name</div>
      <div class="small">00/0, Address Here<br>Road Usa-00000</div>
    </div>
    <div class="body-copy lh-body">
      <p>Lorem ipsum dolor sit amet, consectetuer adipiscing elit, sed diam nonummy nibh euismod tincidunt ut laoreet dolore magna aliquam erat volutpat. Ut wisi enim ad minim veniam, quis nostrud exerci tation ullamcorper suscipit lobortis nisl ut aliquip i</p>
      <p>Lorem ipsum dolor sit amet, cons ectetuer adipiscing elit, sed diam nonummy nibh euismod tincidunt ut laoreet dolore magna aliquam erat volutpat. Ut wisi enim ad minim veniam, quis nostrud exerci tation ullamcorper suscipit lobortis nisl ut aliquip ex ea commodo consequat.</p>
      <p>Lorem ipsum dolor sit amet, consectetuer adipiscing elit, sed diam nonummy nibh euismod tincidunt ut laoreet dolore magna aliquam erat volutpat. Ut wisi enim ad minim veniam, quis nostrud exerci tation</p>
      <p>Lorem ipsum dolor sit amet, consectetuer adipiscing elit, sed diam nonummy nibh euismod tincidunt ut laoreet dolore magna aliquam erat volutpat. Ut wisi enim ad minim veniam, quis nostrud exerci tation</p>
    </div>
    <div class="lh-sign" role="img" aria-label="Handwritten signature"></div>
    <div class="lh-sign-line"></div>
    <div class="lh-to" style="top:313px"><div class="strong">Name Surname</div><div class="small">Position Here</div></div>
  </div>

  <!-- Envelope -->
  <div class="section-label" style="left:453px;top:62px">ENVELOPE</div>
  <div class="sheet envelope-back" style="left:452px;top:109px;width:312px;height:161px">
    <svg class="art" viewBox="0 0 312 161" preserveAspectRatio="none">
      <path d="M0 0H312V8Q312 55 270 55H42Q0 55 0 8Z" fill="var(--navy)"/>
      <path d="M0 101Q100 150 198 161H0Z" fill="var(--red)"/>
      <path d="M0 110Q100 152 180 161H0Z" fill="var(--orange)"/>
      <path d="M0 124Q90 155 150 161H0Z" fill="var(--blue)"/>
    </svg>
  </div>
  <div class="sheet envelope-front" style="left:452px;top:304px;width:308px;height:161px">
    <svg class="art" viewBox="0 0 308 161" preserveAspectRatio="none">
      <defs><linearGradient id="win" x1="0" y1="0" x2="0" y2="1"><stop offset="0" stop-color="#f2f2f2"/><stop offset="1" stop-color="#c9c9c9"/></linearGradient></defs>
      <path d="M0 142Q170 100 308 34V48Q170 120 0 152Z" fill="var(--red)"/>
      <path d="M0 150Q170 118 308 46V60Q170 132 0 156Z" fill="var(--orange)"/>
      <path d="M0 156Q180 130 308 58V161H0Z" fill="var(--blue)"/>
      <rect x="144" y="79" width="136" height="60" rx="5" fill="url(#win)"/>
    </svg>
    <div class="brand" style="left:17px;top:28px;font-size:9.5px"><span class="dot" style="width:9px;height:9px"></span>Veltrium</div>
    <div class="contact" style="left:33px;top:60px;font-size:6.5px;width:110px;height:45px">
      <svg style="left:-10px;top:1px" viewBox="0 0 10 10"><path d="M2 1l2 0 1 2-1 1q1 2 3 3l1-1 2 1 0 2q-7 0-8-8z" fill="var(--orange)"/></svg>
      <div class="row" style="top:0">(123) 456-789</div>
      <svg style="left:-10px;top:12px" viewBox="0 0 10 10"><rect x="1" y="2" width="8" height="6" fill="var(--orange)"/><path d="M1 2l4 3 4-3" stroke="#fff" fill="none" stroke-width=".8"/></svg>
      <div class="row" style="top:11px">email@veltrium.com</div>
      <svg style="left:-10px;top:22px" viewBox="0 0 10 10"><path d="M5 9Q1 5 1 3.5a4 4 0 0 1 8 0Q9 5 5 9z" fill="var(--orange)"/><circle cx="5" cy="3.5" r="1.3" fill="#fff"/></svg>
      <div class="row" style="top:21px">Your Address Here<br>United States, 00000</div>
    </div>
  </div>

  <!-- Business card -->
  <div class="section-label" style="left:231px;top:508px">BUSINESS CARD</div>
  <div class="sheet card-front" style="left:225px;top:544px;width:174px;height:99px;background:linear-gradient(135deg,var(--navy-deep),var(--blue))">
    <svg class="art" viewBox="0 0 174 99" preserveAspectRatio="none">
      <path d="M50 99Q130 88 174 56V64Q130 92 80 99Z" fill="var(--red)"/>
      <path d="M70 99Q135 90 174 64V70Q140 92 95 99Z" fill="var(--orange)"/>
      <path d="M95 99Q145 92 174 70V99Z" fill="#fff"/>
    </svg>
    <div class="brand" style="left:24px;top:38px;font-size:12px;color:#fff"><span class="dot" style="width:11px;height:11px"></span>Veltrium</div>
  </div>
  <div class="sheet card-back" style="left:433px;top:544px;width:174px;height:99px">
    <svg class="art" viewBox="0 0 174 99" preserveAspectRatio="none">
      <rect x="0" y="22" width="3" height="15" fill="var(--navy)"/>
      <path d="M70 99Q135 88 174 63V71Q135 94 95 99Z" fill="var(--red)"/>
      <path d="M95 99Q145 90 174 71V99Z" fill="var(--blue)"/>
    </svg>
    <div class="abs" style="left:23px;top:23px;font-size:8px;font-weight:500;color:var(--navy)">Name Here</div>
    <div class="abs" style="left:23px;top:33px;font-size:3.5px;letter-spacing:.6px;color:#555">FOUNDER</div>
    <div class="abs" style="left:23px;top:39px;width:28px;height:.6px;background:#555"></div>
    <div class="contact" style="left:23px;top:48px;font-size:5px;width:70px;height:40px">
      <svg style="left:-9px;top:1px;width:4px;height:4px" viewBox="0 0 10 10"><path d="M2 1l2 0 1 2-1 1q1 2 3 3l1-1 2 1 0 2q-7 0-8-8z" fill="var(--orange)"/></svg>
      <div class="row" style="top:0">(123) 456-789</div>
      <svg style="left:-9px;top:13px;width:4px;height:4px" viewBox="0 0 10 10"><rect x="1" y="2" width="8" height="6" fill="var(--orange)"/></svg>
      <div class="row" style="top:12px">email@veltrium.com</div>
      <svg style="left:-9px;top:23px;width:4px;height:4px" viewBox="0 0 10 10"><path d="M5 9Q1 5 1 3.5a4 4 0 0 1 8 0Q9 5 5 9z" fill="var(--orange)"/></svg>
      <div class="row" style="top:22px">Your Address Here<br>United States, 00000</div>
    </div>
    <div class="abs" style="left:124px;top:20px;width:18px;height:18px;border-radius:50%;background:var(--orange)"></div>
    <div class="abs" style="left:112px;top:43px;font-size:7px;font-weight:700;color:var(--navy)">Veltrium</div>
  </div>

  <!-- Marketing presentation -->
  <div class="section-label" style="left:322px;top:719px">MARKETING PRESENTATION</div>
  <div class="sheet flyer" style="left:117px;top:745px;width:281px;height:397px">
    <svg class="art" viewBox="0 0 281 397" preserveAspectRatio="none">
      <defs><linearGradient id="cityA" x1="0" y1="0" x2="1" y2="1"><stop offset="0" stop-color="var(--blue-light)"/><stop offset="1" stop-color="var(--navy)"/></linearGradient></defs>
      <path d="M0 204Q120 250 281 276V288Q120 266 0 224Z" fill="var(--red)"/>
      <path d="M0 218Q120 262 281 284V289Q120 270 0 230Z" fill="var(--orange)"/>
      <path d="M0 237Q130 278 281 287V397H0Z" fill="url(#cityA)" role="img" aria-label="City office towers photograph in blue tones"/>
    </svg>
    <div class="brand" style="left:26px;top:17px;font-size:9px"><span class="dot" style="width:9px;height:9px"></span>Veltrium</div>
    <div class="headline" style="left:26px;top:57px;font-size:20px">LOREM IPSUM</div>
    <div class="subline" style="left:26px;top:84px;font-size:10px">PROJECT ASSURANCE<br>AND MONITORING</div>
    <div class="rule" style="left:26px;top:116px;width:56px"></div>
    <div class="body-copy" style="left:25px;top:129px;width:107px;font-size:5px;line-height:6.4px">Lorem ipsum dolor sit amet, consectetuer adipiscing elit, sed diam nonummy nibh euismod tincidunt ut laoreet dolore magna aliquam erat volutpat. Ut wisi enim ad minim veniam, quis nostrud exerci tation ullamcorper suscipit lobortis nisl ut aliquip ex ea commodo consequat. Duis autem vel eum iriure dolor in hendrerit in vulputate velit esse molestie consequat, vel illum dolore eu feugiat nulla facilisis at vero eros et accumsan et iusto odio</div>
    <div class="body-copy" style="left:150px;top:129px;width:106px;font-size:5px;line-height:6.4px">Lorem ipsum dolor sit amet, consectetuer adipiscing elit, sed diam nonummy nibh euismod tincidunt ut laoreet dolore magna aliquam erat volutpat. Ut wisi enim ad minim veniam, quis nostrud exerci tation ullamcorper suscipit lobortis nisl ut aliquip ex ea commodo consequat. Duis autem vel eum iriure dolor in hendrerit in vulputate velit esse molestie consequat, vel illum dolore eu feugiat nulla facilisis at vero eros et accumsan et iusto odio dignissim qui blandit praesent luptatum zzril delenit augue duis dolore te feugait nulla facilisi. Lorem ipsum dolor sit amet, cons ectetuer adipiscing elit, sed diam nonummy nibh euismod tincidunt ut laoreet dolore magna aliquam erat volutpat. Ut wisi enim ad</div>
    <div class="feature" style="left:25px;top:303px;width:110px">
      <h4>⚙ Marketing</h4>
      <p style="padding-left:13px">Lorem ipsum dolor sit amet, consectetur adipiscing elit. Donec vel dui suscipit mi porta condimentum. Maecenas eu porta est. Praesent hendrerit velit a nunc cursus convallis.</p>
    </div>
    <div class="feature" style="left:162px;top:303px;width:95px">
      <h4>› Development</h4>
      <p style="padding-left:15px">Lorem ipsum dolor sit amet, consectetur adipiscing elit. Donec vel dui suscipit mi porta condimentum. Maecenas eu porta est. Praesent hendrerit velit a nunc cursus convallis.</p>
    </div>
    <div class="feature" style="left:25px;top:348px;width:112px">
      <h4>🔒︎ Ideas</h4>
      <p style="padding-left:13px">Lorem ipsum dolor sit amet, consectetur adipiscing elit. Donec vel dui suscipit mi porta condimentum. Maecenas eu porta est. Praesent hendrerit velit a nunc cursus convallis.</p>
    </div>
    <svg class="abs" style="left:170px;top:360px" width="100" height="24" viewBox="0 0 100 24">
      <g fill="none" stroke="#fff" stroke-width="1">
        <path d="M8 2l5 2v4q0 5-5 7-5-2-5-7V4z"/><path d="M6 8l2 2 3-3"/>
        <line x1="27" y1="2" x2="27" y2="18"/>
        <circle cx="51" cy="8" r="5"/><circle cx="51" cy="8" r="2"/>
        <line x1="70" y1="2" x2="70" y2="18"/>
        <path d="M82 11q-3-2-3-5a4 4 0 0 1 8 0q0 3-3 5z"/><line x1="82" y1="13" x2="86" y2="13"/>
      </g>
    </svg>
    <div class="mini-icon" style="left:161px;top:377px">ASSURANCE</div>
    <div class="mini-icon" style="left:204px;top:377px">MONITORING</div>
    <div class="mini-icon" style="left:238px;top:377px">INSIGHT</div>
  </div>

  <div class="sheet slide-cover" style="left:430px;top:766px;width:293px;height:168px">
    <svg class="art" viewBox="0 0 293 168" preserveAspectRatio="none">
      <defs><linearGradient id="cityB" x1="0" y1="0" x2="1" y2="1"><stop offset="0" stop-color="var(--blue-light)"/><stop offset="1" stop-color="var(--navy)"/></linearGradient></defs>
      <path d="M90 168Q210 100 255 0H263Q225 110 120 168Z" fill="var(--red)"/>
      <path d="M110 168Q220 105 260 0H265Q228 112 130 168Z" fill="var(--orange)"/>
      <path d="M138 168Q240 100 271 0H293V168Z" fill="url(#cityB)" role="img" aria-label="Skyscraper photograph in blue tones"/>
    </svg>
    <div class="brand" style="left:20px;top:23px;font-size:7.5px"><span class="dot" style="width:8px;height:8px"></span>Veltrium</div>
    <div class="headline" style="left:21px;top:49px;font-size:17px">LOREM IPSUM</div>
    <div class="subline" style="left:20px;top:69px;font-size:8.5px">PROJECT ASSURANCE<br>AND MONITORING</div>
    <div class="rule" style="left:20px;top:96px;width:33px"></div>
    <div class="body-copy" style="left:20px;top:103px;width:110px;font-size:4.4px;line-height:5.5px">Lorem ipsum dolor sit amet, consectetuer adipiscing elit, sed diam nonummy nibh euismod tincidunt ut laoreet dolore magna aliquam erat volutpat. Ut wisi enim ad minim veniam, quis nostrud exerci tation ullamcorper suscipit lobortis nisl ut aliquip ex</div>
  </div>

  <div class="sheet slide-section" style="left:430px;top:968px;width:293px;height:168px">
    <svg class="art" viewBox="0 0 293 168" preserveAspectRatio="none">
      <circle cx="212" cy="68" r="46" fill="#f3f3f3"/>
      <path d="M120 168Q230 140 293 100V110Q230 150 160 168Z" fill="var(--red)"/>
      <path d="M160 168Q240 146 293 110V168Z" fill="var(--blue)"/>
    </svg>
    <div class="headline" style="left:25px;top:18px;font-size:11px">SECTION TITLE HERE</div>
    <div class="body-copy" style="left:25px;top:41px;width:110px;font-size:4.4px;line-height:5.5px;text-align:left">Lorem ipsum dolor sit amet, consectetuer adipiscing elit, sed diam nonummy nibh euismod tincidunt</div>
    <div class="list-item" style="top:64px">
      <div class="ring" style="background:var(--navy)"><svg width="10" height="10" viewBox="0 0 10 10"><path d="M5 1l3 1v3q0 3-3 4-3-1-3-4V2z" fill="none" stroke="#fff" stroke-width=".7"/><path d="M3.6 5l1 1 2-2" fill="none" stroke="#fff" stroke-width=".7"/></svg></div>
      <div><h5>LOREM IPSUM</h5><p>Lorem ipsum dolor sit amet, consectetuer adipiscing elit, sed diam nonummy nibh euismod tincidunt ut laoreet dolore magna</p></div>
    </div>
    <div class="list-item" style="top:93px">
      <div class="ring" style="background:var(--orange)"><svg width="10" height="10" viewBox="0 0 10 10"><path d="M2 8V6M4 8V5M6 8V4M8 8V3" stroke="#fff" stroke-width=".9"/></svg></div>
      <div><h5>LOREM IPSUM</h5><p>Lorem ipsum dolor sit amet, consectetuer adipiscing elit, sed diam nonummy nibh euismod tincidunt ut laoreet dolore magna</p></div>
    </div>
    <div class="list-item" style="top:122px">
      <div class="ring" style="background:var(--navy)"><svg width="10" height="10" viewBox="0 0 10 10"><circle cx="5" cy="5" r="3" fill="none" stroke="#fff" stroke-width=".7"/><circle cx="5" cy="5" r="1.2" fill="none" stroke="#fff" stroke-width=".7"/></svg></div>
      <div><h5>LOREM IPSUM</h5><p>Lorem ipsum dolor sit amet, consectetuer adipiscing elit, sed diam nonummy nibh euismod tincidunt ut laoreet dolore magna</p></div>
    </div>
  </div>
</div>
</body>
</html>
```